Bref créative
Modern Business Card for Computer Service Company
Brightwave Tech Partners, Inc.
Professional
Marcus T. Hollings
Technology Engineer
4195 Larkin Avenue
Hollywood FL 33024
marcus@btp-helpdesk.com
www.btp-helpdesk.com
I would like a blurb that says "Supporting South Florida Small Business"

```html
<!DOCTYPE html>
<html lang="en">
<head>
<meta charset="utf-8">
<title>Brightwave Tech Partners – Business Card</title>
<link href="https://fonts.googleapis.com/css2?family=Open+Sans:ital,wght@0,400;0,600;0,800;1,400&display=swap" rel="stylesheet">
<style>
  :root{
    --bg:#e9e9ea;
    --card-white:#ffffff;
    --blue-deep:#0b3f8f;
    --blue:#1565c8;
    --blue-light:#3a8fe0;
    --green:#5cb82e;
    --green-light:#8fd14f;
    --ink:#4a4a4a;
    --ink-soft:#7a7a7a;
    --strip:#1c1c1c;
    --white:#ffffff;
  }
  *{margin:0;padding:0;box-sizing:border-box}
  html,body{width:1200px;height:838px;overflow:hidden}
  body{
    background:radial-gradient(ellipse at center,#f6f6f7 0%,var(--bg) 70%);
    font-family:"Open Sans",Arial,sans-serif;
    position:relative;
  }
  .card{
    position:absolute;top:265px;width:540px;height:309px;
    border-radius:3px;overflow:hidden;
    box-shadow:0 10px 28px rgba(0,0,0,.18);
  }
  .card svg.card-art{position:absolute;inset:0;width:100%;height:100%}
  .card-front{left:40px;background:var(--card-white)}
  .card-back{left:620px;background:var(--blue)}

  .brand{position:absolute;display:flex;align-items:center;gap:10px;white-space:nowrap}
  .brand-mark{width:28px;height:28px;background:var(--blue);flex:none}
  .brand-name{font-weight:800;color:var(--blue);font-size:18px;letter-spacing:.1px;line-height:1}
  .card-front .brand{left:28px;top:102px}

  .address{position:absolute;left:30px;top:172px;font-size:11px;line-height:1.55;color:var(--ink-soft);font-style:italic}
  .contacts{position:absolute;left:226px;top:170px;font-size:11px;line-height:1.9;color:var(--ink);list-style:none}
  .contacts li{display:flex;align-items:center;gap:7px}
  .contacts svg{width:10px;height:10px;fill:var(--ink)}

  .person{position:absolute;right:26px;top:38px;text-align:right;color:var(--white)}
  .person-name{font-size:15px;font-weight:600}
  .person-title{font-size:9.5px;font-style:italic;opacity:.85;margin-top:2px}

  .website{position:absolute;left:0;right:0;bottom:7px;text-align:center;color:#d8d8d8;font-size:11px;letter-spacing:.3px}

  .card-back .brand{left:50px;top:92px}
  .card-back .brand-mark{width:44px;height:44px;background:var(--white)}
  .card-back .brand-name{color:var(--white);font-size:30px}
  .tagline{position:absolute;left:52px;top:154px;color:var(--white);font-weight:800;font-size:13px;letter-spacing:.8px}
</style>
</head>
<body>

<section class="card card-front" aria-label="Business card front">
  <svg class="card-art" viewBox="0 0 540 309" preserveAspectRatio="none" aria-hidden="true">
    <defs>
      <linearGradient id="frontBlue" x1="0" y1="0" x2="1" y2="1">
        <stop offset="0" stop-color="var(--blue-light)"/>
        <stop offset="1" stop-color="var(--blue-deep)"/>
      </linearGradient>
      <linearGradient id="frontGreen" x1="0" y1="0" x2="1" y2="0">
        <stop offset="0" stop-color="var(--green-light)"/>
        <stop offset="1" stop-color="var(--green)"/>
      </linearGradient>
    </defs>
    <path d="M230 0 C320 70 430 118 540 132 V150 C420 142 300 90 205 0Z" fill="url(#frontGreen)"/>
    <path d="M250 0 H540 V128 C430 112 330 68 250 0Z" fill="url(#frontBlue)"/>
    <rect x="0" y="281" width="540" height="28" fill="var(--strip)"/>
  </svg>

  <div class="brand">
    <span class="brand-mark"></span>
    <span class="brand-name">Brightwave Tech Partners</span>
  </div>

  <div class="person">
    <div class="person-name">Marcus T. Hollings</div>
    <div class="person-title">Technology Engineer</div>
  </div>

  <p class="address">4195 Larkin Avenue<br>Hollywood FL 33024</p>

  <ul class="contacts">
    <li><svg viewBox="0 0 10 10"><path d="M2 0.5 L3.6 0.5 L4.3 3 L3.2 3.8 C3.8 5 4.9 6.2 6.2 6.8 L7 5.7 L9.5 6.4 V8 C9.5 9 8.8 9.5 8 9.5 C4 9.3 0.7 6 0.5 2 C0.5 1.2 1.1 0.5 2 0.5Z"/></svg>: 954-555-0142</li>
    <li><svg viewBox="0 0 10 10"><rect x="2.5" y="0.5" width="5" height="9" rx="1"/></svg>: 954-555-0187</li>
    <li><svg viewBox="0 0 10 10"><path d="M0.5 2 H9.5 V8.5 H0.5Z M0.5 2 L5 5.5 L9.5 2" /></svg>: marcus@btp-helpdesk.com</li>
  </ul>

  <p class="website">www.btp-helpdesk.com</p>
</section>

<section class="card card-back" aria-label="Business card back">
  <svg class="card-art" viewBox="0 0 540 309" preserveAspectRatio="none" aria-hidden="true">
    <defs>
      <radialGradient id="backBlue" cx="0.45" cy="0.35" r="0.8">
        <stop offset="0" stop-color="var(--blue-light)"/>
        <stop offset="0.55" stop-color="var(--blue)"/>
        <stop offset="1" stop-color="var(--blue-deep)"/>
      </radialGradient>
      <linearGradient id="backGreen" x1="0" y1="0" x2="1" y2="0">
        <stop offset="0" stop-color="var(--green)"/>
        <stop offset="1" stop-color="var(--green-light)"/>
      </linearGradient>
    </defs>
    <rect width="540" height="309" fill="url(#backBlue)"/>
    <path d="M0 250 C150 230 330 200 540 120 V140 C340 222 160 252 0 268Z" fill="url(#backGreen)"/>
    <path d="M0 268 C160 252 340 222 540 140 V309 H0Z" fill="var(--blue-deep)" opacity=".55"/>
  </svg>

  <div class="brand">
    <span class="brand-mark"></span>
    <span class="brand-name">Brightwave Tech Partners</span>
  </div>
  <p class="tagline">SUPPORTING SOUTH FLORIDA SMALL BUSINESS</p>
</section>

</body>
</html>
```